Please supply a print-ready layered .psd file
- 148mm wide x 105mm deep with 3mm bleed
- CMYK for gloss card

Target Market(s)

Women 25 - 40

Requirements
Must have
• Fun look - heart (casually drawn) - writing (sketch look/feel) in the background and faded to say "Love is patient and kind. Love is not jealous or boastful or proud or rude. It does not demand its own way. It is not irritable, and it keeps no record of being wronged. It does not rejoice about injustice but rejoices whenever the truth wins out. Love never gives up, never loses faith, is always hopeful, and endures through every circumstance."

images/text overlay for the front in bold colour (almost like being branded / tattooed / stamp / seal)

Text:
Front: Chosen and marked by Love (emphasise love)

Back: Save the dates: 6 March, 29 May, 14 August, 27 November
Cost: $10 each event
Time: 7:00pm
Location: The Marlowe, 214 Tolley St, Newcastle 2300
These events are hosted by Haven360 to enable women across the region to inspire and encourage others to make a difference in their relationships and world. Our heart is that we as women develop a deep abiding peace, acceptance and experience the overwhelming embracing love of God.
Nice to have
• pictures of Women having fun / laughing (can get from PixVault - please use low res version until approved and then I will purchase).

See examples given of type (type.jpg) and background text (text.jpg)
Should not have
• not women posing for pictures, smiling at the camera

```html
<!DOCTYPE html>
<html lang="en">
<head>
<meta charset="utf-8">
<title>Wildblooms – Chosen and marked by Love</title>
<link rel="stylesheet" href="https://fonts.googleapis.com/css2?family=Gloria+Hallelujah&family=Reenie+Beanie&family=Bowlby+One&family=Fredoka:wght@500&display=swap">
<style>
  :root {
    --page: #ffffff;
    --ink: #000000;
    --chalk: #ffffff;
    --faded: rgba(255,255,255,0.22);
    --teal: #0e8293;
    --aqua: #2fc3e6;
    --brand: #3a8fd6;
    --heart-line: #d9a6bd;
    --photo-warm-a: #c8a58c;
    --photo-warm-b: #efe3d7;
    --photo-cool-a: #9fc1d6;
    --photo-cool-b: #e4d6c4;
  }
  * { margin: 0; padding: 0; box-sizing: border-box; }
  html, body { width: 873px; height: 1200px; overflow: hidden; background: var(--page); }
  .sheet { position: relative; width: 873px; height: 1200px; background: var(--page); font-family: "Gloria Hallelujah", cursive; }

  .card { position: absolute; left: 72px; width: 703px; box-shadow: 4px 6px 10px rgba(0,0,0,0.45); overflow: hidden; }

  /* front */
  .card--front { top: 65px; height: 461px; background: var(--ink); }
  .verse {
    position: absolute; inset: 0; padding: 2px 8px;
    font-family: "Reenie Beanie", cursive; font-size: 30px; line-height: 28px;
    color: var(--faded); word-break: break-all;
  }
  .love-mark { position: absolute; left: 0; top: 110px; width: 703px; height: 200px; }
  .love-mark__letter {
    position: absolute; top: 40px; font-family: "Bowlby One", sans-serif; font-size: 150px; line-height: 1;
    color: var(--chalk); -webkit-text-stroke: 4px var(--ink); paint-order: stroke fill;
    text-shadow: 6px 6px 0 #555;
  }
  .love-mark__l { left: 38px; }
  .love-mark__ve { left: 420px; letter-spacing: -6px; }
  .love-mark__heart { position: absolute; left: 195px; top: 0; width: 250px; height: 210px; }
  .love-mark__words {
    position: absolute; left: 230px; top: 55px; width: 180px; text-align: center;
    font-size: 21px; line-height: 38px; color: var(--ink);
  }
  .wordmark-front {
    position: absolute; left: 0; width: 100%; top: 330px; text-align: center;
    font-family: "Fredoka", sans-serif; font-weight: 500; font-size: 72px; color: var(--chalk); letter-spacing: 2px;
  }

  .side-label { position: absolute; width: 100%; text-align: center; font-size: 34px; color: var(--teal); }
  .side-label--front { top: 560px; }
  .side-label--back { top: 1150px; line-height: 1; }

  /* back */
  .card--back { top: 635px; height: 487px; background: var(--page); }
  .dates-band { position: absolute; left: 0; top: 0; width: 703px; height: 246px; background: var(--ink); }
  .dates-band__teal { position: absolute; left: 387px; top: 0; width: 316px; height: 246px; background: var(--teal); }
  .photo { position: absolute; }
  .photo--laughing { left: 0; top: 20px; width: 138px; height: 102px; background: linear-gradient(135deg, var(--photo-warm-a), var(--photo-warm-b)); }
  .photo--friends { left: 503px; top: 100px; width: 200px; height: 143px; background: linear-gradient(160deg, var(--photo-cool-b), var(--photo-cool-a)); }
  .event { position: absolute; color: var(--aqua); text-align: center; left: 140px; width: 450px; }
  .event__title { top: 10px; font-size: 36px; }
  .event__dates { top: 62px; font-size: 20px; }
  .event__time { top: 88px; font-size: 30px; }
  .event__cost { top: 146px; font-size: 30px; }
  .event__venue { left: 4px; width: auto; top: 216px; font-size: 20px; text-align: left; }
  .about { position: absolute; left: 4px; top: 252px; width: 700px; font-size: 16px; line-height: 59px; color: var(--ink); }
  .host-name {
    position: absolute; left: 440px; top: 420px; font-size: 40px; line-height: 1; color: var(--brand);
  }
</style>
</head>
<body>
<main class="sheet">
  <section class="card card--front" aria-label="Front of card">
    <p class="verse" aria-hidden="true">Love is patient and kind. Love is not jealous or boastful or proud or rude. It does not demand its own way. It is not irritable, and it keeps no record of being wronged. It does not rejoice about injustice but rejoices whenever the truth wins out. Love never gives up, never loses faith, is always hopeful, and endures through every circumstance. Love is patient and kind. Love is not jealous or boastful or proud or rude. It does not demand its own way. It is not irritable, and it keeps no record of being wronged. It does not rejoice about injustice but rejoices whenever the truth wins out. Love never gives up, never loses faith, is always hopeful, and endures through every circumstance. Love is patient and kind. Love is not jealous or boastful or proud or rude. It does not demand its own way. It is not irritable, and it keeps no record of being wronged.</p>
    <div class="love-mark">
      <span class="love-mark__letter love-mark__l">L</span>
      <svg class="love-mark__heart" viewBox="0 0 250 210" aria-hidden="true">
        <path d="M125 200 C60 150 8 110 12 60 C16 20 60 4 92 18 C108 25 120 38 125 52 C131 36 144 22 162 16 C196 6 240 24 238 66 C236 112 186 152 125 200 Z" fill="var(--chalk)" stroke="var(--heart-line)" stroke-width="4"/>
        <path d="M125 196 C64 148 16 108 18 62 C22 26 62 10 92 24" fill="none" stroke="var(--ink)" stroke-width="2"/>
      </svg>
      <p class="love-mark__words">chosen and marked by</p>
      <span class="love-mark__letter love-mark__ve">VE</span>
    </div>
    <p class="wordmark-front">wildblooms</p>
  </section>
  <p class="side-label side-label--front">front</p>

  <section class="card card--back" aria-label="Back of card">
    <div class="dates-band"><div class="dates-band__teal"></div></div>
    <div class="photo photo--laughing" role="img" aria-label="Photo of two women laughing together"></div>
    <div class="photo photo--friends" role="img" aria-label="Photo of three friends sitting on steps chatting and laughing"></div>
    <p class="event event__title">Save the dates!</p>
    <p class="event event__dates">6 March, 29 May, 14 August, 27 November</p>
    <p class="event event__time">7:00pm</p>
    <p class="event event__cost">$10 each event</p>
    <p class="event event__venue">Where? The Marlowe, 214 Tolley St, Newcastle 2300</p>
    <p class="about">These events are hosted by Haven360 to enable women across the region to<br>inspire and encourage others to make a difference in their relationships and world.<br>Our heart is that we as women develop a deep abiding peace, acceptance<br>and experience the overwhelming embracing love of God.</p>
    <p class="host-name">Haven360</p>
  </section>
  <p class="side-label side-label--back">back</p>
</main>
</body>
</html>
```